TRV Conference Newsletter Postcard

We need a template design for a direct mailer postcard that we are sending to potential attendees. The attached templates include the dimensions of the postcard. It is a panel/map type of postcard so it has 8 surfaces that need to have content on them. The purpose of this project is to get people to sign up and attend our conference in May. I have attached what type of layout we would like to have on each panel of the postcard.

Target Market(s)

Category Managers, Shopper Insights, Shopper Marketing

Industry/Entity Type

Consumer

Font styles to use
Sans Serif

Requirements
Must have
• A fun but clean template that includes designs, graphics, elements that show lists, our agenda, pop up graphics that can show facts and stats.
• An interesting shopper cart graphic that include insights, analytics, data, networking, etc.
Nice to have
• Maybe some fun content based on the conference title.
Should not have
• No animated characters. We want this to be clean and innovative, but fun.

```html
<!DOCTYPE html>
<html lang="en">
<head>
<meta charset="utf-8">
<title>TRV Conference Mailer</title>
<link rel="stylesheet" href="https://fonts.googleapis.com/css2?family=Questrial&family=Roboto+Condensed:ital,wght@0,400;0,700;1,800;1,900&display=swap">
<style>
:root{
  --blue:#1b75bc;
  --blue-dark:#0d4f9c;
  --blue-light:#29a8e0;
  --grey:#c9ccd1;
  --ink:#333;
  --white:#fff;
}
*{margin:0;padding:0;box-sizing:border-box}
html,body{width:1200px;height:776px;overflow:hidden;background:var(--white)}
body{font-family:"Questrial",sans-serif;color:var(--ink)}
.mailer{position:relative;width:1200px;height:776px;overflow:hidden;background:var(--white)}
.decor{position:absolute;inset:0}

/* agenda */
.day-header{position:absolute;width:165px;height:46px;background:var(--blue);color:var(--white);
  font-size:12px;line-height:14px;padding:8px 0 0 22px;display:grid;grid-template-columns:70px auto}
.day-header.wide{font-size:11.5px;padding:12px 0 0 20px}
.day-header::before{content:"";position:absolute;left:0;top:0;border-top:14px solid var(--blue-dark);border-right:14px solid transparent}
.timeline{position:absolute;width:170px}
.timeline::before{content:"";position:absolute;left:9px;top:0;bottom:0;width:2px;background:#555}
.event{position:absolute;left:9px;padding-left:13px}
.event::before{content:"";position:absolute;left:-3px;top:7px;width:8px;height:2px;background:#555}
.event-time{display:block;font-size:14px;color:var(--blue);line-height:16px}
.event-name{display:block;font-size:11px;line-height:13px;color:var(--ink)}
.event-note{display:block;font-size:10.5px;line-height:13px}

.faint-name{position:absolute;left:120px;top:470px;font-size:40px;color:var(--blue);opacity:.08;letter-spacing:2px}

/* brand lockups */
.brand{position:absolute;display:flex;align-items:center;gap:10px;color:var(--blue)}
.brand-dot{width:34px;height:34px;border-radius:50%;background:var(--blue)}

/* cover */
.cover-title{position:absolute;left:610px;top:14px;color:var(--white);font-family:"Roboto Condensed",sans-serif;font-style:italic;font-weight:900;line-height:1;text-transform:uppercase}
.cover-title .l1{display:block;font-size:44px}
.cover-title .l2{display:block;font-size:60px;margin-top:2px}
.cover-title .l3{display:block;font-size:30px;font-weight:800;margin-top:4px}
.stamp-label{position:absolute;left:1097px;top:76px;font-family:"Roboto Condensed",sans-serif;font-size:31px;color:#222}
.address-label{position:absolute;left:655px;top:292px;font-family:"Roboto Condensed",sans-serif;font-size:19px;color:#222}
.contact{position:absolute;left:660px;top:672px;width:310px;text-align:center;font-family:"Roboto Condensed",sans-serif;font-size:12px;line-height:21px;color:#444;font-style:normal}
.contact .web{color:var(--blue-light)}
</style>
</head>
<body>
<div class="mailer">

<svg class="decor" width="1200" height="776" viewBox="0 0 1200 776">
  <defs>
    <linearGradient id="photoTone" x1="0" y1="0" x2="1" y2="1">
      <stop offset="0" stop-color="#2a64c8"/>
      <stop offset=".6" stop-color="#3f8ee6"/>
      <stop offset="1" stop-color="#1a4fa8"/>
    </linearGradient>
    <linearGradient id="mapTone" x1="0" y1="0" x2="1" y2="1">
      <stop offset="0" stop-color="#f1f2ef"/>
      <stop offset="1" stop-color="#e6e9e6"/>
    </linearGradient>
    <clipPath id="coverClip"><rect x="600" y="0" width="600" height="776"/></clipPath>
  </defs>

  <!-- top-left corner swoosh -->
  <path d="M0,78 C40,30 100,8 170,0 L150,0 C90,4 30,30 0,60 Z" fill="var(--blue)"/>
  <path d="M0,100 C50,50 110,22 195,0 L178,0 C100,18 40,48 0,84 Z" fill="var(--grey)"/>

  <!-- bottom swoosh on inner panel -->
  <path d="M372,776 C420,700 500,660 600,655 L600,672 C510,676 440,712 400,776 Z" fill="var(--blue)"/>
  <path d="M400,776 C440,716 510,684 600,680 L600,694 C520,698 460,728 425,776 Z" fill="var(--grey)"/>
  <path d="M425,776 C462,734 525,706 600,702 L600,776 Z" fill="var(--blue-light)"/>

  <!-- cover photo area -->
  <g role="img" aria-label="Photo of a business person using a tablet with digital shopping icons">
    <path d="M600,0 H1080 V170 C990,180 930,205 880,232 H600 Z" fill="url(#photoTone)"/>
  </g>
  <path d="M600,188 L640,228 H600 Z" fill="var(--grey)"/>
  <path d="M880,232 C930,205 990,182 1080,172 V196 C1000,204 940,226 885,258 Z" fill="var(--blue)"/>
  <path d="M885,258 C940,228 1000,206 1080,198 V230 C1010,236 950,256 885,290 Z" fill="var(--grey)"/>

  <!-- map area -->
  <g role="img" aria-label="Road map of the region around the conference venue">
    <rect x="600" y="388" width="600" height="388" fill="url(#mapTone)"/>
  </g>

  <!-- lower cover arcs -->
  <g clip-path="url(#coverClip)">
    <ellipse cx="900" cy="900" rx="500" ry="430" fill="var(--blue)"/>
    <ellipse cx="900" cy="900" rx="490" ry="418" fill="var(--white)"/>
    <ellipse cx="900" cy="900" rx="478" ry="404" fill="var(--grey)"/>
    <ellipse cx="900" cy="900" rx="440" ry="362" fill="var(--white)"/>
    <path d="M1200,560 C1160,620 1140,700 1150,776 H1200 Z" fill="var(--blue)"/>
  </g>

  <!-- brand divider -->
  <line x1="992" y1="300" x2="992" y2="380" stroke="var(--blue-light)" stroke-width="1"/>
</svg>

<!-- inner agenda panel -->
<div class="brand" style="left:250px;top:38px;font-size:20px"><span class="brand-dot"></span>TRV Conference</div>
<div class="faint-name">TRV CONFERENCE</div>

<div class="day-header" style="left:38px;top:105px"><span>Monday<br>5/15</span><span>Main<br>Conference</span></div>
<div class="timeline" style="left:38px;top:150px;height:418px">
  <div class="event" style="top:20px"><span class="event-time">1:00 - 2:15 PM</span><span class="event-name">Speed Networking</span></div>
  <div class="event" style="top:80px"><span class="event-time">2:30 - 3:00 PM</span><span class="event-name">Opening Welcome</span></div>
  <div class="event" style="top:124px"><span class="event-time">3:00 - 3:30 PM</span><span class="event-name">Keynote Speaker</span></div>
  <div class="event" style="top:169px"><span class="event-time">3:30 - 4:00 PM</span><span class="event-name">Keynote Speaker</span></div>
  <div class="event" style="top:213px"><span class="event-time">4:00 - 4:20 PM</span><span class="event-name">Break</span></div>
  <div class="event" style="top:258px"><span class="event-time">4:20 - 5:05 PM</span><span class="event-name">Breakout Sessions</span></div>
  <div class="event" style="top:303px"><span class="event-time">5:15 - 6:15 PM</span><span class="event-name">Solution Provider Demos</span><span class="event-note">3 rounds, 15 min rotations,<br>5 min in between</span></div>
  <div class="event" style="top:370px"><span class="event-time">6:15 - 7:30 PM</span><span class="event-name">Networking Reception<br>&amp; Horsd d ouvers</span></div>
</div>

<div class="day-header" style="left:38px;top:584px"><span>Tuesday<br>5/16</span><span>Main<br>Conference</span></div>
<div class="timeline" style="left:38px;top:630px;height:130px">
  <div class="event" style="top:6px"><span class="event-time">7:00 - 8:30 AM</span><span class="event-name">Networking Breakfast</span></div>
  <div class="event" style="top:51px"><span class="event-time">8:30 - 8:45 AM</span><span class="event-name">The Days Highlights</span></div>
  <div class="event" style="top:95px"><span class="event-time">8:45 - 9:30 AM</span><span class="event-name">Keynote Speaker</span></div>
</div>

<div class="day-header" style="left:226px;top:105px"><span>Tuesday<br>5/16</span><span>Main<br>Conference</span></div>
<div class="timeline" style="left:226px;top:150px;height:608px">
  <div class="event" style="top:20px"><span class="event-time">9:30 - 10:00 AM</span><span class="event-name">Keynote Speaker</span></div>
  <div class="event" style="top:75px"><span class="event-time">10:00 - 10:20 AM</span><span class="event-name">Break</span></div>
  <div class="event" style="top:116px"><span class="event-time">10:20 - 10:50 AM</span><span class="event-name">IP Presentations</span></div>
  <div class="event" style="top:161px"><span class="event-time">11:00 - 11:45 AM</span><span class="event-name">Breakout Sessions</span></div>
  <div class="event" style="top:206px"><span class="event-time">11:45 - 1:00 PM</span><span class="event-name">Networking Lunch</span></div>
  <div class="event" style="top:250px"><span class="event-time">1:00 - 2:35 PM</span><span class="event-name">Solution Provider Demos</span><span class="event-note">3 rounds, 15 min rotations,<br>5 min in between</span></div>
  <div class="event" style="top:318px"><span class="event-time">2:45 - 3:30 PM</span><span class="event-name">Breakout Sessions</span></div>
  <div class="event" style="top:358px"><span class="event-time">3:40 - 4:10 PM</span><span class="event-name">IP Presentations</span></div>
  <div class="event" style="top:399px"><span class="event-time">4:10 - 4:30 PM</span><span class="event-name">Break</span></div>
  <div class="event" style="top:444px"><span class="event-time">4:30 - 5:15 PM</span><span class="event-name">Keynote Speaker</span></div>
  <div class="event" style="top:483px"><span class="event-time">5:15 - 6:30 PM</span><span class="event-name">Networking Reception<br>&amp; Horsd d ouvers</span></div>
  <div class="event" style="top:537px"><span class="event-time">6:30 PM</span><span class="event-name">Open Dinner</span></div>
  <div class="event" style="top:579px"><span class="event-time">8:30 PM</span><span class="event-name">Late Night Event</span></div>
</div>

<div class="day-header wide" style="left:421px;top:105px"><span>Wednesday<br>5/17</span><span>Main<br>Conference</span></div>
<div class="timeline" style="left:421px;top:150px;height:470px">
  <div class="event" style="top:24px"><span class="event-time">7:30 - 9:00 AM</span><span class="event-name">Networking Breakfasr</span></div>
  <div class="event" style="top:83px"><span class="event-time">9:00 - 9:45 AM</span><span class="event-name">Keynote Speaker</span></div>
  <div class="event" style="top:127px"><span class="event-time">9:45 - 10:15 AM</span><span class="event-name">Keynote Speaker</span></div>
  <div class="event" style="top:172px"><span class="event-time">10:15 - 10:30 AM</span><span class="event-name">Break</span></div>
  <div class="event" style="top:217px"><span class="event-time">10:30 - 11:00 AM</span><span class="event-name">IP Presentataion</span></div>
  <div class="event" style="top:276px"><span class="event-time">11:10 - 11:55 AM</span><span class="event-name">Breakout Sessions</span></div>
  <div class="event" style="top:320px"><span class="event-time">11:55 - 1:30 PM</span><span class="event-name">Networking Lunch</span></div>
  <div class="event" style="top:364px"><span class="event-time">1:30 - 3:30 PM</span><span class="event-name">Case Study Workshops</span></div>
  <div class="event" style="top:409px"><span class="event-time">3:30 - 4:15 PM</span><span class="event-name">Keynote Speaker</span></div>
  <div class="event" style="top:454px"><span class="event-time">4:15 - 4:30 PM</span><span class="event-name">Closing Remarks</span></div>
</div>

<!-- cover panel -->
<h1 class="cover-title"><span class="l1">Category</span><span class="l2">Management &amp;</span><span class="l3">Shopper Insights Conference</span></h1>
<div class="stamp-label">Stamp</div>
<div class="address-label">Mailing Address Area</div>

<div class="brand" style="left:1005px;top:322px;font-size:22px"><span class="brand-dot"></span>TRV</div>
<div class="brand" style="left:712px;top:600px;font-size:22px"><span class="brand-dot"></span>TRV Conference</div>

<address class="contact">
  410 Harbor Lane, Suite 300 Riverton, MN 55000<br>
  Phone: 555-014-2290<br>
  Email: members@trvevents.org<br>
  <span class="web">Web: trvconference.example</span>
</address>

</div>
</body>
</html>
```